Industry and Trade -may go complete production

Industrial and Corporate Clothing ecom and showcase web site
see supplier ref sites:
www.grellonworkgear.example.com.au
www.mickysprocket.example.com/,
www.Koradyn.example.com.au
Our logo is a roundal shaped gear cog with an elephant inside it.
Main Objective

Get people to contact us for industrial and corporate wear
order online or contact us for more details on products

Information in seconday pages inmportant and ISO standards etc.
Primary Points:

Must show that we are strong and solid.
Visual imagery is important.
We have many web sites in line and this is a start, see zanterfreight.example.com.au for one of ours.

We need a layout for the home page and internal pages. It's an ecomm retail site! Must sell the products AND our company.

Internal pages would be product description pages.

Each page must present an opportunity for them to contact us.
Updates

http://shop.qvx.example.com/siege-of-marrowfen-a-stonehelm-table-game/detail.php?p=481736&v=qvx_series_crown-of-ashes_games#tabs

has very good features 

Reason: Not Enough Responses. This will open up to a designer doing continuous designs for our company. We had lost our last in house designer and need a new innovative person to create genius.

Hi

This tender has been extended due to non response. 
This is our first look at the system as we had designers inder contract who have now left. There are may web sites etc to be done and this is more of a interview.

It is well worth responding. There are already 6 other projects in the pipline. But we want the best .
Barney ter Haust
Group COO Meridale Carriage Pty Ltd
Sydney Australia.

Target Market(s)

TARGET MARKET:
Tradesmen and Corporations and Government agencies
again see the above web sites they address the same markets
especially grellon.example.com.au

Industry/Entity Type

Industrial

Requirements
Must have
• Strength of company
supply and quality are important
ease of use, grellon.example.com.au can be used for good visual expression.
Nice to have
• extreme images and ease of use in navigation and contact.
look at imagery on grellon web site grellon.example.com.au
font useage: see http://money.quorvix.example.com.au/newsbusiness/wire/5193027/dalvane-signs-11b-grid-agreement for font size usage. clear clean to the point.
Should not have
• kitch

```html
<!DOCTYPE html>
<html lang="en">
<head>
<meta charset="utf-8">
<title>Brackmoor &amp; Supply – Home</title>
<link rel="stylesheet" href="https://fonts.googleapis.com/css2?family=Arimo:ital,wght@0,400;0,700;1,400&family=Open+Sans:wght@400&display=swap">
<style>
  :root {
    --page: #ffffff;
    --navy: #1f2a63;
    --accent: #f7a51c;
    --ink: #222222;
    --maroon: #58303a;
    --maroon-text: #5b3a40;
    --button: #2e1a1a;
    --panel: #efefef;
    --panel-line: #c9c9c9;
    --footer: #2f2f2f;
    --footer-base: #222222;
    --footer-head: #ffffff;
    --footer-link: #8c8c8c;
    --social: #5a6e9e;
  }
  * { margin: 0; padding: 0; box-sizing: border-box; }
  html, body { width: 1200px; height: 1200px; overflow: hidden; background: var(--page); }
  body { position: relative; font-family: "Arimo", Arial, sans-serif; }
  .abs { position: absolute; }

  /* header */
  .brand { left: 103px; top: 57px; display: flex; align-items: center; gap: 6px; }
  .brand-mark { width: 56px; height: 56px; border-radius: 50%; background: var(--navy); }
  .brand-name { font-weight: 700; color: var(--navy); font-size: 23px; line-height: 25px; letter-spacing: -0.3px; }
  .main-nav a { position: absolute; top: 78px; height: 26px; line-height: 26px; font-weight: 700; font-size: 14px; letter-spacing: 0.9px; color: var(--ink); text-decoration: none; white-space: nowrap; }
  .main-nav a.active { background: var(--accent); color: #fff; width: 71px; text-align: center; }

  /* hero */
  .hero { left: 120px; top: 114px; width: 960px; height: 536px;
    background: linear-gradient(180deg, #f4f2f2 0%, #e9e2e3 45%, #6a3a40 60%, #4f2a2f 100%); }
  .hero-edge { left: 1080px; top: 114px; width: 40px; height: 536px; background: #f9f9f9; }
  .hero-caption { left: 120px; top: 530px; width: 472px; height: 85px; background: var(--maroon);
    color: #fff; font-weight: 700; font-size: 37px; line-height: 40px; padding: 3px 0 0 11px; }
  .slider-dots { left: 956px; top: 606px; display: flex; gap: 12px; }
  .slider-dots span { width: 20px; height: 20px; border-radius: 50%; background: radial-gradient(circle at 40% 35%, #d8d8d8, #7a7a7a); }
  .slider-dots span.on::after { content: ""; display: block; width: 8px; height: 8px; margin: 6px; border-radius: 50%; background: #333; }

  /* features */
  .feature-title { top: 681px; font-style: italic; font-size: 20px; line-height: 24px; color: var(--maroon-text); }
  .outlets { left: 120px; top: 749px; width: 367px; height: 168px; background: var(--panel); border: 1px solid var(--panel-line); }
  .outlets-image { left: 102px; top: 738px; width: 226px; height: 176px; background: linear-gradient(135deg, #c9d5e4 0%, #d23a3a 55%, #e2a02c 100%); }
  .outlets-title { left: 337px; top: 784px; font-size: 21px; color: var(--maroon-text); letter-spacing: -0.6px; }
  .outlets-text { left: 338px; top: 810px; font-size: 14px; line-height: 17px; color: var(--maroon-text); letter-spacing: -0.3px; }
  .btn { height: 29px; width: 130px; border-radius: 5px; background: linear-gradient(180deg, #4a2c2c, var(--button)); color: #fff; font-size: 14px; line-height: 29px; text-align: center; letter-spacing: -0.3px; }
  .formal { left: 524px; top: 748px; width: 320px; height: 169px;
    background: linear-gradient(90deg, #1a0c0a 0%, #3a2420 40%, #8c7c74 75%, #2a2020 100%); }
  .formal-title { left: 537px; top: 782px; color: #fff; font-weight: 700; font-size: 20px; line-height: 21px; letter-spacing: -0.5px; }
  .formal-text { left: 539px; top: 830px; color: #fff; font-size: 14px; line-height: 17px; }
  .package { left: 915px; top: 765px; width: 135px; height: 133px; background: linear-gradient(160deg, #e9cf93, #b98f4f); }

  /* footer */
  .site-footer { left: 0; top: 957px; width: 1200px; height: 219px; background: var(--footer); font-family: "Open Sans", Arial, sans-serif; }
  .footer-col { position: absolute; top: 9px; font-size: 11.5px; }
  .footer-col h4 { font-weight: 400; color: var(--footer-head); font-size: 11.5px; line-height: 16px; letter-spacing: 0.3px; margin-bottom: 10px; }
  .footer-col ul { list-style: none; margin-bottom: 12px; }
  .footer-col li { color: var(--footer-link); font-size: 11.5px; line-height: 14.6px; letter-spacing: 0.3px; padding-left: 2px; }
  .social { margin-top: 38px; }
  .social li { display: flex; align-items: center; gap: 7px; line-height: 24px; padding-left: 4px; }
  .social i { width: 16px; height: 16px; background: var(--social); display: inline-block; }
  .footer-base { left: 0; top: 1176px; width: 1200px; height: 24px; background: var(--footer-base); color: #ddd; font-size: 11.5px; letter-spacing: 0.5px; line-height: 24px; }
</style>
</head>
<body>
  <header>
    <div class="abs brand">
      <div class="brand-mark"></div>
      <div class="brand-name">BRACKMOOR<br>&amp;SUPPLY</div>
    </div>
    <nav class="main-nav">
      <a class="active" href="#" style="left:531px">HOME</a>
      <a href="#" style="left:613px">PRODUCTS</a>
      <a href="#" style="left:720px">ABOUT US</a>
      <a href="#" style="left:826px">SHOP</a>
      <a href="#" style="left:892px">CONTACT</a>
      <a href="#" style="left:988px">MY ACCOUNT</a>
    </nav>
  </header>

  <section>
    <div class="abs hero" role="img" aria-label="Photo of a man and a woman wearing maroon corporate shirts"></div>
    <div class="abs hero-edge"></div>
    <h1 class="abs hero-caption">THE BEST CHOISE OF<br>THE CORPORATES</h1>
    <div class="abs slider-dots"><span class="on"></span><span></span><span></span><span></span></div>
  </section>

  <section>
    <p class="abs feature-title" style="left:125px">Top Quality Polos and formalwares in<br>more than 100’s Outlets</p>
    <p class="abs feature-title" style="left:526px">The Choise of the corporate world<br>in fasion and style.</p>
    <p class="abs feature-title" style="left:884px">Top Package of the<br>week</p>

    <div class="abs outlets"></div>
    <div class="abs outlets-image" role="img" aria-label="Fanned stack of striped rugby polo shirts"></div>
    <p class="abs outlets-title">100s of outlets</p>
    <p class="abs outlets-text">choose your style<br>from a large amout<br>of varity</p>
    <div class="abs btn" style="left:342px;top:877px">explore stores</div>

    <div class="abs formal" role="img" aria-label="Man in a black tuxedo and bow tie"></div>
    <p class="abs formal-title">Corporates<br>1st choise</p>
    <p class="abs formal-text">the ultimate<br>formalwear<br>collection</p>
    <div class="abs btn" style="left:703px;top:877px">explore collection</div>

    <div class="abs package" role="img" aria-label="Cardboard package box of the week"></div>
  </section>

  <footer class="abs site-footer">
    <div class="footer-col" style="left:150px">
      <h4>Corporate Products</h4>
      <ul><li>Uniforms</li><li>Shirts</li><li>Pents</li><li>Ties</li><li>Shoes</li></ul>
      <h4>Formal</h4>
      <ul><li>Suites</li><li>Coats</li></ul>
    </div>
    <div class="footer-col" style="left:331px">
      <h4>Industrial Products</h4>
      <ul><li>Industrial Uniforms</li><li>Shirts</li><li>Pents</li><li>Trousers</li><li>Jackets</li></ul>
      <h4>Formal</h4>
      <ul><li>Industrial Kit</li><li>Industrial jacket</li></ul>
    </div>
    <div class="footer-col" style="left:509px">
      <h4>Customer Service</h4>
      <ul><li>Your qoutes</li><li>Request qoutes</li><li>FAQ</li><li>Terms</li><li>Conditions</li></ul>
      <h4>B&amp;S Credits</h4>
      <ul><li>Buy credit</li><li>What are credits ?</li></ul>
    </div>
    <div class="footer-col" style="left:691px">
      <h4>Follow</h4>
      <ul class="social">
        <li><i></i>Chirpline</li>
        <li><i></i>Circlebook</li>
        <li><i></i>ViewStream</li>
      </ul>
    </div>
  </footer>
  <div class="abs footer-base">
    <span class="abs" style="left:152px">Terms &amp; Conditons.</span>
    <span class="abs" style="right:103px">© 2011 Brackmoor &amp; Supply. All rights reserved.</span>
  </div>
</body>
</html>
```